Kestrel Bridge Consulting (KBC) Business Card Design

I would like to create double-sided business cards that contain:
1) Name: Derek Molvane
2) Phone Number: +1 (555) 218-4907
3) Email: Derek.Molvane@KestrelBridgeConsulting.example
4) Website: KestrelBridgeConsulting.example

I would like to include my logo and a color scheme similar to the Varnholt Grand Prix Ostera squad color scheme (black, silver, greenish-blue – but can also include regular blue)

What we do: Our company develops and delivers innovative and pragmatic information technology and cybersecurity risk and compliance solutions for organizations in the commercial market as well as the federal, and state/local sectors.

```html
<!DOCTYPE html>
<html lang="en">
<head>
<meta charset="utf-8">
<title>Kestrel Bridge Consulting — Business Card</title>
<link rel="stylesheet" href="https://fonts.googleapis.com/css2?family=Open+Sans:wght@400;600;700&display=swap">
<style>
  :root {
    --stage: #2a2b2e;
    --navy-deep: #121a2c;
    --navy: #1a2540;
    --silver: #c9ced6;
    --silver-dim: #7d8593;
    --paper: #eeeff1;
    --ink: #1d2436;
    --brand-blue: #1f6fb5;
    --brand-cyan: #3aa9dc;
  }
  * { box-sizing: border-box; margin: 0; padding: 0; }
  html, body {
    width: 1200px; height: 900px; overflow: hidden;
    background: var(--stage);
    font-family: "Open Sans", Arial, sans-serif;
  }
  .stage {
    position: relative; width: 1200px; height: 900px;
    display: flex; align-items: center; justify-content: center; gap: 60px;
  }
  .card {
    position: relative; width: 525px; height: 300px;
    box-shadow: 0 18px 40px rgba(0,0,0,.45);
    overflow: hidden;
  }

  /* Front: dark side */
  .card--front {
    background: linear-gradient(135deg, var(--navy-deep) 0%, var(--navy) 55%, var(--navy-deep) 100%);
  }
  .card__network {
    position: absolute; inset: 0;
    background: radial-gradient(ellipse at 70% 60%, rgba(58,169,220,.28) 0%, rgba(31,53,88,.15) 45%, transparent 75%);
  }
  .brand {
    display: flex; align-items: center; gap: 14px;
  }
  .brand__dot {
    flex: none; border-radius: 50%;
    background: var(--brand-cyan);
  }
  .brand__name {
    font-family: "Open Sans", Arial, sans-serif;
    font-weight: 600; line-height: 1.2; white-space: nowrap;
  }
  .card--front .brand {
    position: absolute; left: 60px; top: 92px;
  }
  .card--front .brand__dot { width: 44px; height: 44px; }
  .card--front .brand__name { font-size: 22px; color: var(--silver); }
  .card__blurb {
    position: absolute; left: 60px; top: 170px; width: 400px;
    font-size: 6.5px; line-height: 1.6; color: var(--silver-dim);
  }
  .card__web {
    position: absolute; left: 60px; top: 208px;
    font-size: 13px; color: var(--silver); letter-spacing: .02em;
  }

  /* Back: white side */
  .card--back { background: var(--paper); }
  .card--back .brand {
    position: absolute; left: 34px; top: 34px; gap: 10px;
  }
  .card--back .brand__dot { width: 28px; height: 28px; background: var(--brand-blue); }
  .card--back .brand__name { font-size: 14px; color: var(--ink); }
  .contact {
    position: absolute; left: 34px; top: 160px;
  }
  .contact__name {
    font-size: 25px; font-weight: 700; color: var(--brand-blue); letter-spacing: .01em;
  }
  .contact__line {
    font-size: 11.5px; color: var(--brand-blue); line-height: 1.6;
  }
  .contact__name + .contact__line { margin-top: 4px; }
</style>
</head>
<body>
  <main class="stage">
    <section class="card card--front" aria-label="Business card front">
      <div class="card__network" role="img" aria-label="Faint hexagonal network pattern in blue tones"></div>
      <div class="brand">
        <span class="brand__dot"></span>
        <span class="brand__name">Kestrel Bridge Consulting</span>
      </div>
      <p class="card__blurb">Pragmatic IT, cybersecurity, risk and compliance solutions for commercial and public sector clients. Delivered with care across federal, state and local agencies.</p>
      <p class="card__web">KestrelBridgeConsulting.example</p>
    </section>

    <section class="card card--back" aria-label="Business card back">
      <div class="brand">
        <span class="brand__dot"></span>
        <span class="brand__name">Kestrel Bridge Consulting</span>
      </div>
      <div class="contact">
        <p class="contact__name">Derek Molvane</p>
        <p class="contact__line">+1 (555) 218-4907</p>
        <p class="contact__line">Derek.Molvane@KestrelBridgeConsulting.example</p>
      </div>
    </section>
  </main>
</body>
</html>
```